Bref créative
Business Card/Letterhead
Brightkey Home Realty
Professional
Daniel Fitch
Sales Manager
42 Wattle Crescent Bellbrae 3228
info@brightkeyhm.com.au
www.brightkeyhm.com.au
058713K
My name, phone number and email address are the most important for the business card with my address to be in smaller font in the bottom of the card.
logo

```html
<!DOCTYPE html>
<html lang="en">
<head>
<meta charset="utf-8">
<title>Brightkey Home Realty – Stationery</title>
<link rel="stylesheet" href="https://fonts.googleapis.com/css2?family=Open+Sans:wght@400;600;700&display=swap">
<style>
  :root {
    --backdrop: #a6a6a6;
    --paper: #ffffff;
    --gold-dark: #9c8d3f;
    --gold-mid: #b8aa5c;
    --gold-light: #d8cf92;
    --navy: #2b3553;
    --rule: #3a3a3a;
    --ink: #333333;
    --shadow: rgba(0,0,0,0.25);
  }
  * { box-sizing: border-box; margin: 0; padding: 0; }
  html, body { width: 1200px; height: 684px; overflow: hidden; }
  body {
    background: var(--backdrop);
    font-family: "Open Sans", Arial, sans-serif;
    color: var(--ink);
    position: relative;
  }
  .sheet {
    position: absolute;
    background: var(--paper);
    box-shadow: 0 1px 4px var(--shadow);
    overflow: hidden;
  }
  .gold-band {
    position: absolute;
    left: 0; right: 0;
    background: linear-gradient(180deg, var(--gold-light) 0%, var(--gold-mid) 45%, var(--gold-dark) 100%);
  }
  .gold-band.top { top: 0; border-bottom: 2px solid var(--rule); }
  .gold-band.bottom { bottom: 0; border-top: 2px solid var(--rule); }

  .brand {
    position: absolute;
    display: flex;
    align-items: center;
    gap: 8px;
    color: var(--navy);
    font-weight: 600;
  }
  .brand-mark {
    background: var(--gold-mid);
    flex: none;
  }
  .brand-name { line-height: 1.05; }
  .brand-name .line1 { display: block; letter-spacing: 0.06em; }
  .brand-name .line2 { display: block; letter-spacing: 0.12em; }

  .footer-line {
    position: absolute;
    display: flex;
    justify-content: space-between;
    font-size: 7px;
    color: var(--ink);
  }

  /* Letterhead */
  .letterhead { left: 180px; top: 19px; width: 485px; height: 646px; }
  .letterhead .gold-band.top { height: 19px; }
  .letterhead .gold-band.bottom { height: 21px; }
  .letterhead .brand { left: 30px; top: 36px; }
  .letterhead .brand-mark { width: 14px; height: 14px; }
  .letterhead .brand-name .line1 { font-size: 22px; }
  .letterhead .brand-name .line2 { font-size: 10px; }
  .letterhead .footer-line { left: 28px; right: 28px; bottom: 30px; }

  /* Business card */
  .business-card { left: 36px; top: 283px; width: 199px; height: 115px; }
  .business-card .gold-band.top { height: 17px; }
  .business-card .gold-band.bottom { height: 17px; }
  .business-card .card-title {
    position: absolute; top: 3px; left: 0; right: 0;
    text-align: center; font-size: 5px; color: var(--navy); font-weight: 600;
  }
  .business-card .brand { left: 26px; top: 26px; gap: 5px; }
  .business-card .brand-mark { width: 8px; height: 8px; }
  .business-card .brand-name .line1 { font-size: 13px; }
  .business-card .brand-name .line2 { font-size: 6px; }
  .business-card .card-contact {
    position: absolute; left: 26px; top: 68px;
    font-size: 5px; line-height: 1.4; color: var(--ink);
  }
  .business-card .card-contact .address { font-size: 4px; }

  /* Envelope back */
  .envelope-back { left: 641px; top: 19px; width: 521px; height: 310px; }
  .envelope-back .flap { position: absolute; left: 0; top: 0; width: 100%; height: 64px; }

  /* Envelope front */
  .envelope-front { left: 643px; top: 372px; width: 519px; height: 235px; }
  .envelope-front .gold-band.top { height: 17px; }
  .envelope-front .gold-band.bottom { height: 19px; }
  .envelope-front .brand { left: 29px; top: 40px; }
  .envelope-front .brand-mark { width: 13px; height: 13px; }
  .envelope-front .brand-name .line1 { font-size: 21px; }
  .envelope-front .brand-name .line2 { font-size: 9px; }
  .envelope-front .footer-line { left: 14px; right: 14px; bottom: 30px; font-size: 6px; }
</style>
</head>
<body>

  <section class="sheet letterhead" aria-label="Letterhead">
    <div class="gold-band top"></div>
    <div class="brand">
      <span class="brand-mark"></span>
      <span class="brand-name"><span class="line1">BRIGHTKEY</span><span class="line2">Home Realty</span></span>
    </div>
    <div class="footer-line">
      <span>Phone: 0438615092 | info@brightkeyhm.com.au</span>
      <span>42 Wattle Crescent Bellbrae 3228 | www.brightkeyhm.com.au</span>
    </div>
    <div class="gold-band bottom"></div>
  </section>

  <section class="sheet business-card" aria-label="Business card">
    <div class="gold-band top"><div class="card-title">Daniel Fitch · Sales Manager</div></div>
    <div class="brand">
      <span class="brand-mark"></span>
      <span class="brand-name"><span class="line1">BRIGHTKEY</span><span class="line2">Home Realty</span></span>
    </div>
    <div class="card-contact">
      <div>Phone: 0438615092 | info@brightkeyhm.com.au</div>
      <div class="address">42 Wattle Crescent Bellbrae 3228</div>
    </div>
    <div class="gold-band bottom"></div>
  </section>

  <section class="sheet envelope-back" aria-label="Envelope back">
    <svg class="flap" viewBox="0 0 521 64" preserveAspectRatio="none" aria-hidden="true">
      <defs>
        <linearGradient id="flapGold" x1="0" y1="0" x2="0" y2="1">
          <stop offset="0" stop-color="#d8cf92"/>
          <stop offset="0.5" stop-color="#b8aa5c"/>
          <stop offset="1" stop-color="#9c8d3f"/>
        </linearGradient>
      </defs>
      <path d="M0 0 H521 V34 Q521 52 503 52 H18 Q0 52 0 34 Z" fill="url(#flapGold)" stroke="#3a3a3a" stroke-width="1.5"/>
    </svg>
  </section>

  <section class="sheet envelope-front" aria-label="Envelope front">
    <div class="gold-band top"></div>
    <div class="brand">
      <span class="brand-mark"></span>
      <span class="brand-name"><span class="line1">BRIGHTKEY</span><span class="line2">Home Realty</span></span>
    </div>
    <div class="footer-line">
      <span>Phone: 0438615092 | info@brightkeyhm.com.au</span>
      <span>42 Wattle Crescent Bellbrae 3228 | www.brightkeyhm.com.au</span>
    </div>
    <div class="gold-band bottom"></div>
  </section>

</body>
</html>
```